Velmint website

A clean uncluttered design that shows at glance that we are in the Media and design and publishing business.

We would like to see designs that use colours that show warmth and quality.

The website should show:
- products
- projects

These should be displaxed in spaces that we can add or interchanges with new products or projects.
Updates

Target Market(s)

Business and project managers and buyers and authors.

Industry/Entity Type

Business

Requirements
Must have
• Good colours. Not too strong, not weak, but reflecting quality.

```html
<!DOCTYPE html>
<html lang="en">
<head>
<meta charset="utf-8">
<title>Velmint – Media &amp; Design Publishing</title>
<link rel="stylesheet" href="https://fonts.googleapis.com/css2?family=Open+Sans:wght@400;600;700&family=Oswald:wght@600;700&display=swap">
<style>
  :root {
    --navy: #0b3a7e;
    --navy-dark: #08306a;
    --cyan: #1db2ea;
    --cyan-link: #27a9e1;
    --text-grey: #6b6b6b;
    --nav-grey: #555a63;
    --light-grey: #ececec;
    --card-border: #ececec;
    --rule: #cfcfcf;
    --white: #ffffff;
    --banner-word: #8d9fe0;
  }
  * { box-sizing: border-box; margin: 0; padding: 0; }
  html, body { width: 937px; height: 1200px; overflow: hidden; background: var(--white); }
  body { position: relative; font-family: "Open Sans", Arial, sans-serif; color: var(--text-grey); }

  /* Header */
  .brand { position: absolute; left: 45px; top: 30px; }
  .brand-name { font-size: 41px; font-weight: 600; color: var(--navy); letter-spacing: -0.5px; line-height: 1; }
  .brand-tagline { font-size: 16px; color: #9a9a9a; margin-top: 4px; line-height: 1; }

  .search { position: absolute; left: 279px; top: 15px; width: 233px; height: 23px; border: 1px solid #dcdcdc; background: var(--white);
    font-size: 11px; color: #a4a4a4; padding: 4px 10px; }
  .search svg { position: absolute; right: 7px; top: 4px; }

  .call-tab { position: absolute; left: 512px; top: 0; width: 381px; height: 40px; }
  .call-text { position: absolute; left: 512px; top: 8px; width: 381px; text-align: center; color: var(--white); font-size: 19px; line-height: 24px; }
  .call-text strong { font-weight: 600; }
  .account-links { position: absolute; left: 560px; top: 44px; width: 290px; text-align: center; font-size: 10.5px; color: var(--navy); letter-spacing: 0.1px; }

  .main-nav { position: absolute; left: 359px; top: 80px; display: flex; font-size: 12.5px; color: var(--nav-grey); letter-spacing: 0.4px; }
  .main-nav span { padding: 0 14px; border-left: 1px solid var(--nav-grey); line-height: 13px; }
  .main-nav span:first-child { border-left: none; padding-left: 0; }
  .main-nav span:last-child { padding-right: 0; }
  .main-nav .is-active { color: #5a86b8; font-weight: 600; }

  /* Hero slider */
  .hero { position: absolute; left: 46px; top: 108px; width: 847px; height: 280px; background: var(--light-grey); }
  .hero-photo { position: absolute; left: 7px; top: 7px; width: 833px; height: 240px;
    background: linear-gradient(90deg, #4a6b9a 0%, #7d93b8 30%, #9a8f96 48%, #2a2a2e 62%, #111114 100%); }
  .hero-word { position: absolute; right: 70px; top: 68px; font-family: "Oswald", Impact, sans-serif; font-weight: 700;
    font-size: 44px; color: var(--banner-word); letter-spacing: 0.5px; }
  .hero-caption { position: absolute; left: 0; bottom: 0; width: 327px; height: 40px; background: rgba(150,150,150,0.75);
    font-family: "Oswald", Impact, sans-serif; font-weight: 600; color: var(--white); font-size: 16px; padding: 9px 0 0 48px; letter-spacing: 0.2px; }
  .hero-arrow { position: absolute; top: 86px; }
  .hero-arrow.prev { left: 25px; }
  .hero-arrow.next { right: 25px; }
  .hero-dots { position: absolute; left: 388px; top: 258px; display: flex; gap: 5px; }
  .hero-dots i { width: 13px; height: 13px; border-radius: 50%; background: var(--navy); display: block; }
  .hero-dots i.is-current { background: var(--white); border: 1.5px solid var(--navy); }

  /* Sections */
  .section-head { position: absolute; left: 47px; width: 846px; height: 20px; display: flex; align-items: center; }
  .section-title { font-size: 16px; color: #6d6d6d; letter-spacing: 0.3px; white-space: nowrap; }
  .section-rule { flex: 1; height: 1px; background: var(--rule); margin: 0 12px 0 16px; }
  .view-more { font-size: 8px; color: #5a7fae; margin-right: 10px; }
  .pager { display: flex; gap: 6px; }

  .product-row { position: absolute; left: 47px; width: 846px; display: grid; grid-template-columns: repeat(6, 124px); column-gap: 20.4px; }
  .product { display: flex; flex-direction: column; align-items: flex-end; }
  .product-card { width: 124px; height: 234px; border: 5px solid var(--card-border); background: var(--white); padding: 12px 7px 0 3px; position: relative; }
  .product-cover { width: 109px; height: 145px; }
  .cover-battle { background: linear-gradient(180deg, #7b8a92 0%, #4d5150 45%, #5b3a22 80%, #c05d1f 100%); }
  .cover-number { background: linear-gradient(180deg, #b46a3c 0%, #6b5a58 40%, #c9a25a 75%, #2a6fa8 100%); }
  .cover-saga { background: linear-gradient(180deg, #3f8b46 0%, #2e7a3a 50%, #4c9850 100%); }
  .cover-bird { background: linear-gradient(180deg, #f3f4f6 0%, #e8e9ec 50%, #e9c3a7 70%, #eef0f3 100%); border: 1px solid #e2e2e2; }
  .product-name { font-size: 9.5px; line-height: 14px; color: var(--cyan-link); margin-top: 14px; width: 98px; }
  .product-price { font-size: 9.5px; font-weight: 700; color: #222; margin-top: 2px; }
  .product-go { position: absolute; right: 5px; bottom: 17px; }
  .buy-now { margin-top: 10px; width: 60px; height: 21px; background: var(--navy); color: var(--white); font-size: 10.5px; font-weight: 600;
    text-align: center; line-height: 21px; letter-spacing: 0.2px; }

  /* Footer */
  .site-footer { position: absolute; left: 0; top: 1140px; width: 937px; height: 60px; background: var(--navy-dark); color: var(--white); }
  .footer-links { position: absolute; left: 48px; top: 12px; font-size: 9.5px; line-height: 18px; letter-spacing: 0.2px; }
  .copyright { position: absolute; right: 51px; top: 16px; font-size: 11.5px; display: flex; align-items: center; gap: 6px; }
</style>
</head>
<body>

<header class="site-header">
  <div class="brand">
    <div class="brand-name">VELMINT</div>
    <div class="brand-tagline">Media &amp; Design Publishing</div>
  </div>

  <div class="search">Search entire store here...
    <svg width="14" height="14" viewBox="0 0 14 14" aria-hidden="true"><circle cx="7" cy="7" r="6" fill="none" stroke="#c8c8c8"/><path d="M4 7h6M8 5l2 2-2 2" stroke="#8a8a8a" fill="none"/></svg>
  </div>

  <svg class="call-tab" viewBox="0 0 381 40" aria-hidden="true">
    <polygon points="0,0 381,0 337,38 46,38" fill="#0b3a7e"/>
  </svg>
  <svg style="position:absolute;left:540px;top:38px" width="322" height="26" viewBox="0 0 322 26" aria-hidden="true">
    <polygon points="18,0 309,0 295,24 40,24" fill="#ececec"/>
  </svg>
  <div class="call-text">Call Us : <strong>1-855-204-7310</strong></div>
  <div class="account-links">SIGN UP | SIGN IN | VIEW CART | MY WISHLIST</div>

  <nav class="main-nav">
    <span class="is-active">HOME</span><span>ABOUTUS</span><span>PRODUCTS</span><span>PROJECTS</span><span>FOR AUTHOR</span><span>CONTACTS</span>
  </nav>
</header>

<section class="hero">
  <div class="hero-photo" role="img" aria-label="Climber hanging from a dark rock overhang against an evening sky">
    <div class="hero-word">CHALLENGE</div>
    <div class="hero-caption">FEATURED PROJECTS</div>
    <svg class="hero-arrow prev" width="20" height="76" viewBox="0 0 20 76" aria-hidden="true"><path d="M17 2 L4 38 L17 74" stroke="#fff" stroke-width="3" fill="none"/></svg>
    <svg class="hero-arrow next" width="20" height="76" viewBox="0 0 20 76" aria-hidden="true"><path d="M3 2 L16 38 L3 74" stroke="#fff" stroke-width="3" fill="none"/></svg>
  </div>
  <div class="hero-dots"><i class="is-current"></i><i></i><i></i><i></i></div>
</section>

<section class="section-head" style="top:413px">
  <h2 class="section-title" style="font-weight:400">NEW PRODUCTS</h2>
  <div class="section-rule"></div>
  <span class="view-more">VIEW MORE</span>
  <div class="pager">
    <svg width="19" height="19" viewBox="0 0 19 19" aria-hidden="true"><circle cx="9.5" cy="9.5" r="9.5" fill="#0b3a7e"/><path d="M11 5.5 L7 9.5 L11 13.5" stroke="#fff" stroke-width="2" fill="none"/></svg>
    <svg width="19" height="19" viewBox="0 0 19 19" aria-hidden="true"><circle cx="9.5" cy="9.5" r="9.5" fill="#0b3a7e"/><path d="M8 5.5 L12 9.5 L8 13.5" stroke="#fff" stroke-width="2" fill="none"/></svg>
  </div>
</section>

<div class="product-row" style="top:450px">
  <div class="product"><div class="product-card"><div class="product-cover cover-battle" role="img" aria-label="Film cover: soldier walking through a burning city"></div><p class="product-name">Lorem ipsum dolor sit amet.</p><p class="product-price">$12.58</p><svg class="product-go" width="13" height="13" viewBox="0 0 13 13" aria-hidden="true"><circle cx="6.5" cy="6.5" r="6.5" fill="#1db2ea"/><path d="M3.5 6.5h5M6.5 4l2.5 2.5-2.5 2.5" stroke="#fff" stroke-width="1.3" fill="none"/></svg></div><div class="buy-now">BUY NOW</div></div>
  <div class="product"><div class="product-card"><div class="product-cover cover-number" role="img" aria-label="Film cover: three young heroes above a glowing title"></div><p class="product-name">Lorem ipsum dolor sit amet.</p><p class="product-price">$12.58</p><svg class="product-go" width="13" height="13" viewBox="0 0 13 13" aria-hidden="true"><circle cx="6.5" cy="6.5" r="6.5" fill="#1db2ea"/><path d="M3.5 6.5h5M6.5 4l2.5 2.5-2.5 2.5" stroke="#fff" stroke-width="1.3" fill="none"/></svg></div><div class="buy-now">BUY NOW</div></div>
  <div class="product"><div class="product-card"><div class="product-cover cover-battle" role="img" aria-label="Film cover: soldier walking through a burning city"></div><p class="product-name">Lorem ipsum dolor sit amet.</p><p class="product-price">$12.58</p><svg class="product-go" width="13" height="13" viewBox="0 0 13 13" aria-hidden="true"><circle cx="6.5" cy="6.5" r="6.5" fill="#1db2ea"/><path d="M3.5 6.5h5M6.5 4l2.5 2.5-2.5 2.5" stroke="#fff" stroke-width="1.3" fill="none"/></svg></div><div class="buy-now">BUY NOW</div></div>
  <div class="product"><div class="product-card"><div class="product-cover cover-saga" role="img" aria-label="Book cover: green fantasy novel with a golden helmet"></div><p class="product-name">Lorem ipsum dolor sit amet.</p><p class="product-price">$12.58</p><svg class="product-go" width="13" height="13" viewBox="0 0 13 13" aria-hidden="true"><circle cx="6.5" cy="6.5" r="6.5" fill="#1db2ea"/><path d="M3.5 6.5h5M6.5 4l2.5 2.5-2.5 2.5" stroke="#fff" stroke-width="1.3" fill="none"/></svg></div><div class="buy-now">BUY NOW</div></div>
  <div class="product"><div class="product-card"><div class="product-cover cover-bird" role="img" aria-label="Book cover: white play script with a painted bird"></div><p class="product-name">Lorem ipsum dolor sit amet.</p><p class="product-price">$12.58</p><svg class="product-go" width="13" height="13" viewBox="0 0 13 13" aria-hidden="true"><circle cx="6.5" cy="6.5" r="6.5" fill="#1db2ea"/><path d="M3.5 6.5h5M6.5 4l2.5 2.5-2.5 2.5" stroke="#fff" stroke-width="1.3" fill="none"/></svg></div><div class="buy-now">BUY NOW</div></div>
  <div class="product"><div class="product-card"><div class="product-cover cover-number" role="img" aria-label="Film cover: three young heroes above a glowing title"></div><p class="product-name">Lorem ipsum dolor sit amet.</p><p class="product-price">$12.58</p><svg class="product-go" width="13" height="13" viewBox="0 0 13 13" aria-hidden="true"><circle cx="6.5" cy="6.5" r="6.5" fill="#1db2ea"/><path d="M3.5 6.5h5M6.5 4l2.5 2.5-2.5 2.5" stroke="#fff" stroke-width="1.3" fill="none"/></svg></div><div class="buy-now">BUY NOW</div></div>
</div>

<section class="section-head" style="top:780px">
  <h2 class="section-title" style="font-weight:400">LATEST&nbsp; PROJECTS</h2>
  <div class="section-rule"></div>
  <span class="view-more">VIEW MORE</span>
  <div class="pager">
    <svg width="19" height="19" viewBox="0 0 19 19" aria-hidden="true"><circle cx="9.5" cy="9.5" r="9.5" fill="#0b3a7e"/><path d="M11 5.5 L7 9.5 L11 13.5" stroke="#fff" stroke-width="2" fill="none"/></svg>
    <svg width="19" height="19" viewBox="0 0 19 19" aria-hidden="true"><circle cx="9.5" cy="9.5" r="9.5" fill="#0b3a7e"/><path d="M8 5.5 L12 9.5 L8 13.5" stroke="#fff" stroke-width="2" fill="none"/></svg>
  </div>
</section>

<div class="product-row" style="top:818px">
  <div class="product"><div class="product-card"><div class="product-cover cover-battle" role="img" aria-label="Film cover: soldier walking through a burning city"></div><p class="product-name">Lorem ipsum dolor sit amet.</p><p class="product-price">$12.58</p><svg class="product-go" width="13" height="13" viewBox="0 0 13 13" aria-hidden="true"><circle cx="6.5" cy="6.5" r="6.5" fill="#1db2ea"/><path d="M3.5 6.5h5M6.5 4l2.5 2.5-2.5 2.5" stroke="#fff" stroke-width="1.3" fill="none"/></svg></div><div class="buy-now">BUY NOW</div></div>
  <div class="product"><div class="product-card"><div class="product-cover cover-number" role="img" aria-label="Film cover: three young heroes above a glowing title"></div><p class="product-name">Lorem ipsum dolor sit amet.</p><p class="product-price">$12.58</p><svg class="product-go" width="13" height="13" viewBox="0 0 13 13" aria-hidden="true"><circle cx="6.5" cy="6.5" r="6.5" fill="#1db2ea"/><path d="M3.5 6.5h5M6.5 4l2.5 2.5-2.5 2.5" stroke="#fff" stroke-width="1.3" fill="none"/></svg></div><div class="buy-now">BUY NOW</div></div>
  <div class="product"><div class="product-card"><div class="product-cover cover-battle" role="img" aria-label="Film cover: soldier walking through a burning city"></div><p class="product-name">Lorem ipsum dolor sit amet.</p><p class="product-price">$12.58</p><svg class="product-go" width="13" height="13" viewBox="0 0 13 13" aria-hidden="true"><circle cx="6.5" cy="6.5" r="6.5" fill="#1db2ea"/><path d="M3.5 6.5h5M6.5 4l2.5 2.5-2.5 2.5" stroke="#fff" stroke-width="1.3" fill="none"/></svg></div><div class="buy-now">BUY NOW</div></div>
  <div class="product"><div class="product-card"><div class="product-cover cover-saga" role="img" aria-label="Book cover: green fantasy novel with a golden helmet"></div><p class="product-name">Lorem ipsum dolor sit amet.</p><p class="product-price">$12.58</p><svg class="product-go" width="13" height="13" viewBox="0 0 13 13" aria-hidden="true"><circle cx="6.5" cy="6.5" r="6.5" fill="#1db2ea"/><path d="M3.5 6.5h5M6.5 4l2.5 2.5-2.5 2.5" stroke="#fff" stroke-width="1.3" fill="none"/></svg></div><div class="buy-now">BUY NOW</div></div>
  <div class="product"><div class="product-card"><div class="product-cover cover-bird" role="img" aria-label="Book cover: white play script with a painted bird"></div><p class="product-name">Lorem ipsum dolor sit amet.</p><p class="product-price">$12.58</p><svg class="product-go" width="13" height="13" viewBox="0 0 13 13" aria-hidden="true"><circle cx="6.5" cy="6.5" r="6.5" fill="#1db2ea"/><path d="M3.5 6.5h5M6.5 4l2.5 2.5-2.5 2.5" stroke="#fff" stroke-width="1.3" fill="none"/></svg></div><div class="buy-now">BUY NOW</div></div>
  <div class="product"><div class="product-card"><div class="product-cover cover-number" role="img" aria-label="Film cover: three young heroes above a glowing title"></div><p class="product-name">Lorem ipsum dolor sit amet.</p><p class="product-price">$12.58</p><svg class="product-go" width="13" height="13" viewBox="0 0 13 13" aria-hidden="true"><circle cx="6.5" cy="6.5" r="6.5" fill="#1db2ea"/><path d="M3.5 6.5h5M6.5 4l2.5 2.5-2.5 2.5" stroke="#fff" stroke-width="1.3" fill="none"/></svg></div><div class="buy-now">BUY NOW</div></div>
</div>

<footer class="site-footer">
  <div class="footer-links">
    Customer Service | About us | Terms &amp; Conditions | Sitemap | Contact Us<br>
    Looking Authors | Products | Sign In | View Cart | My Wishlist | Help
  </div>
  <div class="copyright">
    COPYRIGHT 2014
    <svg width="16" height="16" viewBox="0 0 16 16" aria-hidden="true"><circle cx="8" cy="8" r="7" fill="none" stroke="#fff" stroke-width="1.3"/><path d="M10.5 6a3 3 0 1 0 0 4" fill="none" stroke="#fff" stroke-width="1.3"/></svg>
    VELMINT.COM
  </div>
</footer>

</body>
</html>
```